harbor institute of business and technology web site

I need web site for the institute which focus on business courses and computer course it is also for vocation train for employment It is also carear development and advancement .It should have links to online study resource which free
Industry/Entity Type
Business
Number of Pages Required
1 page
Look and feel
Each slider illustrates characteristics of the customer's brand and the style your logo design should communicate.

```html
<!DOCTYPE html>
<html lang="en">
<head>
<meta charset="utf-8">
<title>Harbor Institute of Business and Technology</title>
<link href="https://fonts.googleapis.com/css2?family=Open+Sans:wght@400;600;700&display=swap" rel="stylesheet">
<style>
:root{
  --blue:#1e9ad6;
  --blue-dark:#1479b0;
  --navy:#1d2a4d;
  --ink:#333;
  --muted:#8a8f96;
  --panel:#3a3d42;
  --panel-dark:#2c2e32;
  --footer:#2a2c2f;
  --black:#161718;
  --yellow:#f2c200;
  --white:#fff;
  --line:#d7dbe0;
}
*{box-sizing:border-box;margin:0;padding:0}
html,body{width:1200px;height:2524px;overflow:hidden}
body{font-family:"Open Sans",Arial,sans-serif;color:var(--ink);background:var(--white);position:relative}
section,header,footer,nav{position:absolute;left:0;width:1200px}

/* header */
.site-header{top:0;height:112px;background:var(--white)}
.brand{position:absolute;left:60px;top:26px;display:flex;align-items:center;gap:12px}
.brand-mark{width:40px;height:40px;background:var(--blue)}
.brand-name{font-weight:700;font-size:26px;color:var(--blue);letter-spacing:1px}
.main-nav{position:absolute;left:420px;top:56px;display:flex;height:56px}
.main-nav a{display:block;padding:0 20px;line-height:56px;font-size:15px;font-weight:600;color:var(--ink);text-decoration:none}
.main-nav a.active{background:#2b2c2e;color:var(--white)}
.register{position:absolute;right:60px;top:14px;background:var(--blue);color:var(--white);font-size:11px;font-weight:700;padding:6px 14px;letter-spacing:.5px}
.socials{position:absolute;right:60px;top:50px;display:flex;gap:8px}
.socials span{width:26px;height:26px;border-radius:50%;background:var(--blue)}

/* hero */
.hero{top:112px;height:416px}
.hero-photo{position:absolute;inset:0;background:linear-gradient(100deg,#e9eef2 0%,#c6d3dc 35%,#9fb3c2 60%,#c9d6de 100%)}
.hero-title{position:absolute;left:560px;top:120px;color:var(--white);font-size:28px;font-weight:600;line-height:38px;text-align:center;text-shadow:0 1px 3px rgba(0,0,0,.25)}

/* feature boxes */
.features{top:528px;height:176px;background:var(--panel);display:flex}
.feature{flex:1;padding:24px 30px;border-right:1px solid #4b4f55;text-align:center;color:#c8ccd1}
.feature:last-child{border-right:none}
.feature h3{font-size:20px;font-weight:400;color:var(--white);line-height:24px}
.feature h3 b{display:block;color:var(--blue);font-weight:400}
.feature p{font-size:12px;line-height:17px;margin-top:12px}

/* welcome */
.welcome{top:720px;height:330px;background:var(--blue);color:var(--white)}
.welcome h2{position:absolute;top:26px;width:100%;text-align:center;font-size:30px;font-weight:400;letter-spacing:1px}
.welcome h2 b{font-weight:700}
.welcome-photo{position:absolute;left:80px;top:80px;width:380px;height:220px;background:linear-gradient(160deg,#d9e3ea,#8fa5b5 60%,#5e7384)}
.welcome-text{position:absolute;left:500px;top:84px;width:620px;font-size:13px;line-height:20px}
.pillars{position:absolute;left:500px;top:176px;display:flex;gap:60px}
.pillar{display:flex;gap:14px;width:260px}
.pillar .ico{flex:none;width:54px;height:54px;border-radius:50%;border:2px solid var(--white);display:flex;align-items:center;justify-content:center}
.pillar h4{font-size:16px;font-weight:600}
.pillar p{font-size:12px;line-height:17px}
.read-more{position:absolute;left:500px;top:272px;font-size:11px;font-weight:700;letter-spacing:.5px}

/* core values */
.values{top:1050px;height:500px;background:var(--white)}
.section-title{text-align:center;font-size:34px;font-weight:400;color:var(--ink);letter-spacing:1px}
.values .section-title{position:absolute;top:80px;width:100%}
.values .rule{position:absolute;left:540px;top:136px;width:120px;height:2px;background:var(--blue)}
.value{position:absolute;top:250px;width:180px;text-align:center}
.value .disc{width:140px;height:140px;margin:0 auto;border-radius:50%;border:6px solid #e4e7ea;background:var(--white);display:flex;align-items:center;justify-content:center}
.value.active .disc{background:#2f3236;border-color:#cfd3d7}
.value span{display:block;margin-top:20px;font-size:16px;line-height:21px;color:var(--ink)}
.arrow{position:absolute;top:300px}

/* programs */
.programs{top:1560px;height:400px}
.programs-photo{position:absolute;inset:0;background:linear-gradient(120deg,#3b4752,#1f272e 55%,#36434d)}
.programs .section-title{position:absolute;top:30px;width:100%;color:var(--white)}
.cards{position:absolute;left:120px;top:110px;display:flex;gap:20px}
.card{width:225px;background:rgba(0,0,0,.6);text-align:center;color:var(--white)}
.card h3{background:var(--blue);font-size:16px;font-weight:600;line-height:20px;padding:12px 0}
.card p{font-size:12px;line-height:17px;padding:18px 20px 10px;color:#dde2e6}
.card .go{width:40px;height:40px;margin:6px auto 18px;border-radius:50%;background:var(--yellow);display:flex;align-items:center;justify-content:center}
.slide-arrow{position:absolute;top:180px}

/* inquiry */
.inquiry{top:1960px;height:200px;background:var(--white)}
.inquiry h2{position:absolute;left:150px;top:56px;font-size:32px;line-height:34px;font-weight:400;color:var(--blue);text-align:right}
.inquiry h2 b{display:block;color:var(--navy);font-weight:700}
.field{position:absolute;height:36px;border:1px solid var(--line);background:#f7f8f9;display:flex;align-items:center;gap:8px;padding:0 10px;font-size:12px;color:var(--muted)}
.field i{width:14px;height:14px;background:var(--blue);display:block}
.submit{position:absolute;left:900px;top:108px;width:120px;height:36px;background:var(--navy);color:var(--white);font-size:13px;font-weight:700;text-align:center;line-height:36px}

/* footer */
.footer-nav{top:2160px;height:48px;background:#3d3f43;display:flex;justify-content:center;gap:48px}
.footer-nav a{line-height:48px;color:var(--white);font-size:13px;font-weight:600;text-decoration:none}
.footer-main{top:2208px;height:272px;background:var(--footer);color:#c8ccd1}
.footer-main h4{font-size:16px;font-weight:600;color:var(--white);letter-spacing:.5px;margin-bottom:18px}
.col{position:absolute;top:36px}
.news-item{display:flex;gap:12px;margin-bottom:16px;width:220px;font-size:12px;line-height:16px}
.news-item .date{flex:none;width:44px;background:var(--white);color:var(--ink);font-size:10px;font-weight:700;text-align:center;line-height:14px;padding:4px 0}
.contact-line{display:flex;gap:12px;align-items:flex-start;font-size:12px;line-height:17px;margin-bottom:12px;width:300px}
.contact-line svg{flex:none;margin-top:2px}
.foot-social{display:flex;gap:8px;margin-bottom:14px}
.foot-social span{width:30px;height:30px;border-radius:50%;background:var(--blue)}
.newsletter label{display:block;font-size:12px;margin-bottom:8px}
.newsletter .row{display:flex}
.newsletter .input{width:140px;height:28px;background:var(--white);font-size:11px;color:var(--muted);line-height:28px;padding-left:8px}
.newsletter .btn{width:36px;height:28px;background:var(--yellow);color:var(--ink);font-size:11px;font-weight:700;text-align:center;line-height:28px}
.partner{position:absolute;left:970px;top:36px;width:170px;border:1px solid #4a4d52;padding:16px;text-align:center}
.partner p{font-size:11px;font-weight:700;color:var(--yellow);letter-spacing:.5px}
.partner .badge{width:130px;height:44px;margin:12px auto 0;background:var(--white);border-radius:4px}
.copyright{top:2480px;height:44px;background:var(--black);color:#9ca1a7;font-size:12px;text-align:center;line-height:44px}
</style>
</head>
<body>

<header class="site-header">
  <div class="brand"><span class="brand-mark"></span><span class="brand-name">HARBOR INSTITUTE</span></div>
  <nav class="main-nav" style="position:absolute;width:auto">
    <a class="active" href="#">HOME</a><a href="#">ABOUT US</a><a href="#">PROGRAMS</a><a href="#">RESOURCES</a><a href="#">NEWS</a><a href="#">CONTACT US</a>
  </nav>
  <div class="register">ONLINE REGISTRATION</div>
  <div class="socials"><span></span><span></span><span></span><span></span><span></span></div>
</header>

<section class="hero">
  <div class="hero-photo" role="img" aria-label="Student working at a digital screen interface with the institute crest on the right"></div>
  <h1 class="hero-title">Acquire Applied Knowledge,<br>Embrace Possibilities</h1>
</section>

<section class="features">
  <div class="feature"><h3>TECHNICAL<b>EDUCATION</b></h3><p>Hands-on computer and engineering courses built for real jobs.</p></div>
  <div class="feature"><h3>BUSINESS<b>EDUCATION</b></h3><p>Practical business courses in finance, marketing and management.</p></div>
  <div class="feature"><h3>ONLINE<b>EDUCATION</b></h3><p>Free online study resources you can use any time.</p></div>
  <div class="feature"><h3>SKILLS<b>DEVELOPMENT</b></h3><p>Vocational training for employment and career advancement.</p></div>
</section>

<section class="welcome">
  <h2>WELCOME TO <b>HARBOR INSTITUTE</b></h2>
  <div class="welcome-photo" role="img" aria-label="Computer lab with rows of desktop workstations"></div>
  <p class="welcome-text">Harbor Institute offers business and computer courses for learners at every stage. Our vocational training prepares students for employment, while our career development programs help working people grow and advance. Free online study resources support learning beyond the classroom.</p>
  <div class="pillars">
    <div class="pillar">
      <div class="ico"><svg width="26" height="26" viewBox="0 0 26 26"><circle cx="13" cy="13" r="10" fill="none" stroke="#fff" stroke-width="2"/><circle cx="13" cy="13" r="5" fill="none" stroke="#fff" stroke-width="2"/><circle cx="13" cy="13" r="1.5" fill="#fff"/></svg></div>
      <div><h4>Our Mission</h4><p>To deliver applied learning that opens doors to work.</p></div>
    </div>
    <div class="pillar">
      <div class="ico"><svg width="28" height="20" viewBox="0 0 28 20"><path d="M2 10 Q14 -4 26 10 Q14 24 2 10Z" fill="none" stroke="#fff" stroke-width="2"/><circle cx="14" cy="10" r="4" fill="#fff"/></svg></div>
      <div><h4>Our Vision</h4><p>A skilled community ready for a changing world.</p></div>
    </div>
  </div>
  <div class="read-more">READ MORE ABOUT HARBOR &rsaquo;</div>
</section>

<section class="values">
  <h2 class="section-title">OUR CORE VALUES</h2>
  <div class="rule"></div>
  <svg class="arrow" style="left:56px" width="20" height="36" viewBox="0 0 20 36"><path d="M16 2 L4 18 L16 34" fill="none" stroke="#9aa0a6" stroke-width="3"/></svg>
  <svg class="arrow" style="left:1124px" width="20" height="36" viewBox="0 0 20 36"><path d="M4 2 L16 18 L4 34" fill="none" stroke="#9aa0a6" stroke-width="3"/></svg>
  <div class="value active" style="left:94px">
    <div class="disc"><svg width="56" height="56" viewBox="0 0 56 56"><circle cx="28" cy="22" r="16" fill="none" stroke="#fff" stroke-width="3"/><path d="M28 12 l3 7 7 .5 -5.5 4.5 2 7 -6.5-4 -6.5 4 2-7 -5.5-4.5 7-.5z" fill="#fff"/><path d="M18 36 L14 52 L22 48 L26 54 L28 38 M38 36 L42 52 L34 48 L30 54 L28 38" fill="#fff"/></svg></div>
    <span>Excellence</span>
  </div>
  <div class="value" style="left:302px">
    <div class="disc"><svg width="56" height="50" viewBox="0 0 56 50"><path d="M28 46 L6 24 A12 12 0 0 1 28 8 A12 12 0 0 1 50 24 Z" fill="var(--blue)"/></svg></div>
    <span>Integrity</span>
  </div>
  <div class="value" style="left:510px">
    <div class="disc"><svg width="56" height="56" viewBox="0 0 56 56"><path d="M8 50 L28 6 L48 50 L38 50 L28 26 L18 50Z" fill="var(--blue)"/></svg></div>
    <span>Respect</span>
  </div>
  <div class="value" style="left:718px">
    <div class="disc"><svg width="56" height="60" viewBox="0 0 56 60"><path d="M28 6 A16 16 0 0 1 38 35 L38 42 L18 42 L18 35 A16 16 0 0 1 28 6Z" fill="var(--blue)"/><rect x="20" y="46" width="16" height="4" fill="var(--blue)"/><rect x="22" y="53" width="12" height="4" fill="var(--blue)"/></svg></div>
    <span>Disruptive<br>Innovation</span>
  </div>
  <div class="value" style="left:926px">
    <div class="disc"><svg width="56" height="56" viewBox="0 0 56 56"><g fill="var(--blue)"><rect x="24" y="4" width="8" height="48"/><rect x="24" y="4" width="8" height="48" transform="rotate(45 28 28)"/><rect x="24" y="4" width="8" height="48" transform="rotate(90 28 28)"/><rect x="24" y="4" width="8" height="48" transform="rotate(135 28 28)"/><circle cx="28" cy="28" r="16"/></g><circle cx="28" cy="28" r="7" fill="#fff"/></svg></div>
    <span>Bias For<br>Action</span>
  </div>
</section>

<section class="programs">
  <div class="programs-photo" role="img" aria-label="Students studying at laptops in a classroom"></div>
  <h2 class="section-title">OUR PROGRAMS OFFERED</h2>
  <svg class="slide-arrow" style="left:70px" width="20" height="36" viewBox="0 0 20 36"><path d="M16 2 L4 18 L16 34" fill="none" stroke="#fff" stroke-width="3"/></svg>
  <svg class="slide-arrow" style="left:1110px" width="20" height="36" viewBox="0 0 20 36"><path d="M4 2 L16 18 L4 34" fill="none" stroke="#fff" stroke-width="3"/></svg>
  <div class="cards">
    <div class="card"><h3>Certificate<br>Programs</h3><p>Short focused courses that lead to a recognised certificate.</p><div class="go"><svg width="14" height="16" viewBox="0 0 14 16"><path d="M3 2 L11 8 L3 14" fill="none" stroke="#333" stroke-width="3"/></svg></div></div>
    <div class="card"><h3>Diploma<br>Programs</h3><p>One-year programs combining theory with workplace practice.</p><div class="go"><svg width="14" height="16" viewBox="0 0 14 16"><path d="M3 2 L11 8 L3 14" fill="none" stroke="#333" stroke-width="3"/></svg></div></div>
    <div class="card"><h3>Advanced<br>Programs</h3><p>Specialist training for professionals seeking career growth.</p><div class="go"><svg width="14" height="16" viewBox="0 0 14 16"><path d="M3 2 L11 8 L3 14" fill="none" stroke="#333" stroke-width="3"/></svg></div></div>
    <div class="card"><h3>Degree<br>Programs</h3><p>Full degree pathways in business and technology fields.</p><div class="go"><svg width="14" height="16" viewBox="0 0 14 16"><path d="M3 2 L11 8 L3 14" fill="none" stroke="#333" stroke-width="3"/></svg></div></div>
  </div>
</section>

<section class="inquiry">
  <h2>QUICK<b>INQUIRY</b></h2>
  <div class="field" style="left:420px;top:58px;width:250px"><i></i>Name</div>
  <div class="field" style="left:690px;top:58px;width:250px"><i></i>Email Address</div>
  <div class="field" style="left:960px;top:58px;width:180px"><i></i>Phone</div>
  <div class="field" style="left:420px;top:108px;width:460px"><i></i>Message</div>
  <div class="submit">SUBMIT</div>
</section>

<nav class="footer-nav">
  <a href="#">HOME</a><a href="#">ABOUT US</a><a href="#">PROGRAMS</a><a href="#">RESOURCES</a><a href="#">NEWS</a><a href="#">CONTACT US</a>
</nav>

<footer class="footer-main">
  <div class="col" style="left:120px">
    <h4>LATEST NEWS</h4>
    <div class="news-item"><div class="date">12<br>OCT</div><p>New computer lab opens for evening classes.</p></div>
    <div class="news-item"><div class="date">03<br>OCT</div><p>Enrolment now open for the next intake.</p></div>
  </div>
  <div class="col" style="left:440px">
    <h4>CONTACT INFO</h4>
    <div class="contact-line"><svg width="14" height="18" viewBox="0 0 14 18"><path d="M7 17 C2 10 1 8 1 6 A6 6 0 0 1 13 6 C13 8 12 10 7 17Z" fill="var(--blue)"/><circle cx="7" cy="6" r="2" fill="#2a2c2f"/></svg><p>Plot No. 42 Quayside Complex, Marine Road, Westhaven</p></div>
    <div class="contact-line"><svg width="14" height="16" viewBox="0 0 14 16"><path d="M3 1 L6 1 L7 5 L5 6.5 A9 9 0 0 0 8.5 10 L10 8 L13 9 L13 13 Q13 15 11 15 A11 11 0 0 1 1 4 Q1 1 3 1Z" fill="var(--blue)"/></svg><p>+1 555 0142 880</p></div>
    <div class="contact-line"><svg width="16" height="12" viewBox="0 0 16 12"><rect x="0.5" y="0.5" width="15" height="11" fill="var(--blue)"/><path d="M1 1 L8 7 L15 1" fill="none" stroke="#2a2c2f" stroke-width="1.5"/></svg><p>info@harborinstitute.example</p></div>
  </div>
  <div class="col" style="left:760px">
    <div class="foot-social"><span></span><span></span><span></span><span></span></div>
    <div class="newsletter"><label>Newsletter Sign Up</label><div class="row"><div class="input">Email address</div><div class="btn">Go</div></div></div>
  </div>
  <div class="partner"><p>IN CONJUNCTION WITH</p><div class="badge"></div></div>
</footer>

<div class="copyright" style="position:absolute;left:0;width:1200px">Copyright 2015 &middot; Harbor Technology Institute | All Right Reserved</div>

</body>
</html>
```